Brava Stone Oven Kitchen (restaurant)

Restaurant with a cool vibe.
We need a refresh of existing site. Appealing to a hip crowd of 25 or older age bracket (mid price to high small town). Constant changes food and cocktail menu. A vibing atmosphere with jazz funk hip music.
Must be able to scale for any device… phone/mobile device super important.
Instagram: @Brava.Linwell
Website: bravalinwell.example

Target Market(s)

25-55 age group

Number of Pages Required

1 page

Font styles to use
Sans Serif

Requirements
Must have
• Simple to navigate. Simplicity is the key to all sophistication.

Links/Buttons
Menu
Gift Cards
Reservations
Take Out
Contact Us
Should not have
• Please, nothing generic looking… no cookie cutter look. Originality

```html
<!DOCTYPE html>
<html lang="en">
<head>
<meta charset="utf-8">
<title>Brava Stone Oven Kitchen</title>
<link href="https://fonts.googleapis.com/css2?family=Poppins:ital,wght@0,300;0,400;0,500;0,600;0,700;0,800;1,300&display=swap" rel="stylesheet">
<style>
:root{
  --red:#ff0000;
  --red-deep:#e60b0b;
  --ink:#1a1a1a;
  --text:#6f6f6f;
  --white:#ffffff;
  --footer:#141414;
  --line:#e4e4e4;
}
*{margin:0;padding:0;box-sizing:border-box}
html,body{width:1200px;height:3979px;overflow:hidden}
body{position:relative;background:var(--white);font-family:'Poppins',sans-serif;color:var(--ink)}
.abs{position:absolute}
.heading{font-family:'Poppins',sans-serif;font-weight:700;line-height:1;letter-spacing:-1px}

/* hero */
.hero-bg{left:0;top:0;width:1200px;height:727px;background:linear-gradient(100deg,#1d1510 0%,#2b1f17 45%,#4a2e1e 70%,#6b3a22 100%)}
.hero-food{left:520px;top:40px;width:680px;height:687px;background:radial-gradient(ellipse at 55% 45%,#8a3a1f 0%,#5a2c1a 40%,rgba(43,31,23,0) 75%)}
.brand{left:111px;top:40px;color:var(--white);font-size:19px;font-weight:600;display:flex;align-items:center;gap:10px}
.brand .mark{width:12px;height:12px;background:var(--white);border-radius:50%}
.nav{left:520px;top:47px;display:flex;gap:26px;font-size:11px;font-weight:500;color:var(--white);text-transform:uppercase;white-space:nowrap}
.nav .active{position:relative}
.nav .active::after{content:"";position:absolute;left:-6px;right:-6px;top:31px;height:2px;background:var(--red)}
.nav-rule{left:514px;top:84px;width:606px;height:1px;background:rgba(255,255,255,.15)}
.social-top{left:1052px;top:50px;display:flex;gap:19px}
.social-top span{width:9px;height:9px;border-radius:50%;background:var(--white)}
.hero-title{left:112px;top:232px;font-size:100px;color:var(--white);letter-spacing:-2px}
.hero-text{left:119px;top:366px;width:450px;font-size:16px;line-height:31px;color:var(--white)}
.btn{display:flex;align-items:center;justify-content:center;font-size:11px;font-weight:500;text-transform:uppercase;letter-spacing:.3px}
.btn-light{background:var(--white);color:var(--ink)}
.btn-red{background:var(--red);color:var(--white)}

/* about */
.about-frame{left:128px;top:845px;width:360px;height:339px;border:4px solid var(--red)}
.about-photo{left:159px;top:868px;width:358px;height:336px;background:linear-gradient(135deg,#c9b99a 0%,#d8a43a 40%,#b8675a 70%,#7d6a4e 100%)}
.eyebrow{font-size:20px;letter-spacing:5px;color:#333;font-weight:400}
.about-text{left:647px;top:995px;width:380px;font-size:14px;line-height:25px;color:var(--text)}

/* menu */
.menu-bg{left:0;top:1350px;width:1200px;height:728px;background:linear-gradient(90deg,#2c3a2a 0%,#8b7a66 20%,#b67a3a 60%,#5a4a3a 100%)}
.menu-panel{left:60px;top:1403px;width:1090px;height:638px;background:rgba(255,10,10,.93);border:2px solid rgba(255,255,255,.6)}
.menu-text{left:310px;top:1558px;width:580px;text-align:center;font-size:14px;line-height:25px;color:var(--white)}
.tab{top:1660px;width:145px;height:97px;border:2px solid var(--white);color:var(--white);display:flex;flex-direction:column;align-items:center;justify-content:flex-end;padding-bottom:12px;gap:10px;font-size:16px;letter-spacing:1.5px;text-transform:uppercase}
.tab.is-active{background:var(--white);color:#222}
.tab svg{width:36px;height:36px}
.dish{display:flex;align-items:center;font-size:14px;color:var(--white);height:20px}
.dish .dots{flex:1;border-bottom:2px dotted rgba(255,255,255,.7);margin:0 14px;transform:translateY(3px)}
.dish .price{white-space:nowrap}
.col-left .dish{width:440px}
.col-right .dish{width:475px}
.col-left .dish .price{width:50px}
.col-right .dish .price{width:90px}
.arrow{top:1981px;width:65px;height:60px;background:var(--white);display:flex;align-items:center;justify-content:center}

/* testimonials */
.center-x{left:0;width:1200px;text-align:center}
.testi-text{top:2299px;font-size:14px;line-height:25px;color:var(--text);font-style:italic;font-weight:300}
.avatar{left:566px;top:2394px;width:50px;height:50px;border-radius:50%;background:linear-gradient(#c9b2a0,#7d6a5c)}
.quote-badge{left:613px;top:2402px;width:34px;height:34px;border-radius:50%;background:var(--red);border:3px solid var(--white)}
.person{top:2475px;font-size:19px;font-weight:600}
.person small{font-size:14px;color:var(--red);font-weight:400;margin-left:12px}
.dot{top:2546px;width:11px;height:11px;border-radius:50%;border:2px solid var(--red)}
.dot.on{background:var(--red)}

/* gallery */
.tile{top:2636px;width:240px;height:228px}
.tile-red{background:var(--red-deep);color:var(--white);text-align:center;display:flex;flex-direction:column;justify-content:center;gap:8px}
.tile-red h4{font-size:20px;font-weight:600}
.tile-red p{font-size:12px;line-height:19px;padding:0 36px}

/* contact */
.contact-text{left:125px;top:3068px;width:400px;font-size:14px;line-height:25px;color:var(--text)}
.field{border:1px solid var(--line);font-size:12px;color:#666;padding:0 22px;display:flex;align-items:center}
.field.area{align-items:flex-start;padding-top:24px}
.map-frame{left:755px;top:2968px;width:358px;height:495px;border:4px solid var(--red)}
.map{left:735px;top:2992px;width:349px;height:496px;background:linear-gradient(160deg,#ececec,#e2e5e4)}

/* footer */
.footer-rule{left:0;top:3594px;width:1200px;height:8px;background:var(--red)}
.footer{left:0;top:3602px;width:1200px;height:377px;background:var(--footer)}
.footer-brand{left:131px;top:3690px;font-size:19px;font-weight:600;color:var(--white)}
.f-small{font-size:12px;color:#c8c8c8}
.f-head{font-size:16px;font-weight:600;color:var(--white)}
.f-contact{display:flex;align-items:center;gap:10px}
.soc{top:3843px;width:34px;height:34px;border-radius:50%}
.f-link{font-size:11px;color:#c8c8c8;width:105px;padding-bottom:8px;border-bottom:1px solid #2e2e2e;text-transform:uppercase}
</style>
</head>
<body>

<!-- Hero -->
<div class="hero-bg abs" role="img" aria-label="Photo of grilled steak, vegetables and spices on a dark wooden table"></div>
<div class="hero-food abs" role="img" aria-label="Board of grilled meat and peppers"></div>
<div class="brand abs"><span class="mark"></span>Brava Stone Oven Kitchen</div>
<nav class="nav abs">
  <span class="active">Home</span><span>Menu</span><span>Reservations</span><span>Gift Cards</span><span>Order Online</span><span>Contact</span>
</nav>
<div class="nav-rule abs"></div>
<div class="social-top abs" aria-label="Social links"><span></span><span></span><span></span></div>
<h1 class="hero-title heading abs">Restaurant</h1>
<p class="hero-text abs">Lorem Ipsum is simply dummy text of the printing and typesetting industry. Lorem Ipsum has been the industry's standard dummy</p>
<div class="btn btn-light abs" style="left:119px;top:494px;width:133px;height:36px">Our Menu</div>
<div class="btn btn-red abs" style="left:272px;top:494px;width:133px;height:36px">Book a Table</div>

<!-- About -->
<section class="about">
  <div class="about-frame abs"></div>
  <div class="about-photo abs" role="img" aria-label="Photo of a pressed sandwich with ham, cheese and pickles"></div>
  <div class="eyebrow abs" style="left:647px;top:862px">WELCOME</div>
  <h2 class="heading abs" style="left:645px;top:912px;font-size:54px">About Us</h2>
  <p class="about-text abs">Lorem Ipsum is simply dummy text of the printing and typesetting industry. Lorem Ipsum has been the industry's standard dummy text ever since the 1500s, when an unknown printer took a galley.</p>
  <div class="btn btn-red abs" style="left:647px;top:1139px;width:134px;height:35px">Read More</div>
</section>

<!-- Menu -->
<section class="menu">
  <div class="menu-bg abs" role="img" aria-label="Photo of dishes and dips on a woven tablecloth"></div>
  <div class="menu-panel abs"></div>
  <h2 class="heading center-x abs" style="top:1472px;font-size:54px;color:var(--white)">Menu</h2>
  <p class="menu-text abs">Lorem Ipsum is simply dummy text of the printing and typesetting industry. Lorem Ipsum has been the industry's standard dummy</p>

  <div class="tab is-active abs" style="left:369px">
    <svg viewBox="0 0 36 36" fill="none" stroke="#222" stroke-width="1.5"><path d="M9 14h18l-2 18H11z"/><path d="M13 14V5M17 14V3M21 14V5M25 14V7"/><path d="M14 24a4 4 0 0 0 8 0"/></svg>
    Take Out
  </div>
  <div class="tab abs" style="left:531px">
    <svg viewBox="0 0 36 36" fill="none" stroke="#fff" stroke-width="1.5"><path d="M9 17a9 7 0 0 1 18 0z"/><path d="M8 20h20M9 24h18a2 2 0 0 1-2 4H11a2 2 0 0 1-2-4z"/><path d="M2 14h5M1 18h5M2 22h5"/></svg>
    Dinner
  </div>
  <div class="tab abs" style="left:693px">
    <svg viewBox="0 0 36 36" fill="none" stroke="#fff" stroke-width="1.5"><path d="M9 12h18l-2 21H11z"/><path d="M8 9h20v3H8z"/><path d="M20 9l3-7"/><circle cx="18" cy="22" r="4"/></svg>
    Juices
  </div>

  <div class="col-left abs" style="left:124px;top:1806px">
    <div class="dish"><span>Shareables</span><span class="dots"></span><span class="price">$ 11.99</span></div>
    <div class="dish" style="margin-top:5px"><span>Salads</span><span class="dots"></span><span class="price">$ 10.99</span></div>
    <div class="dish" style="margin-top:29px"><span>Burgers</span><span class="dots"></span><span class="price">$ 11.50</span></div>
    <div class="dish" style="margin-top:5px"><span>Stone Oven Pizza</span><span class="dots"></span><span class="price">$ 10.99</span></div>
  </div>
  <div class="col-right abs" style="left:627px;top:1806px">
    <div class="dish"><span>Sandwiches</span><span class="dots"></span><span class="price">$ 9.50</span></div>
    <div class="dish" style="margin-top:5px"><span>Mains &amp; Pasta</span><span class="dots"></span><span class="price">Market Price</span></div>
    <div class="dish" style="margin-top:29px"><span>Local Caught Shrimp</span><span class="dots"></span><span class="price">Market Price</span></div>
    <div class="dish" style="margin-top:5px"><span>Atchafalaya</span><span class="dots"></span><span class="price">$ 10.99</span></div>
  </div>

  <div class="arrow abs" style="left:545px"><svg width="14" height="18" viewBox="0 0 14 18" fill="none" stroke="#222" stroke-width="1.6"><path d="M10 2 3 9l7 7"/></svg></div>
  <div class="arrow abs" style="left:613px"><svg width="14" height="18" viewBox="0 0 14 18" fill="none" stroke="#222" stroke-width="1.6"><path d="m4 2 7 7-7 7"/></svg></div>
</section>

<!-- Testimonials -->
<section class="testimonials">
  <div class="eyebrow center-x abs" style="top:2174px">TESTIMONIALS</div>
  <h2 class="heading center-x abs" style="top:2226px;font-size:54px">Customer Reviews</h2>
  <p class="center-x testi-text abs">Lorem Ipsum is simply dummy text of the printing<br>and typesetting industry. Lorem Ipsum has been the industry's standard dummy</p>
  <div class="avatar abs" role="img" aria-label="Customer portrait"></div>
  <div class="quote-badge abs"><svg width="28" height="28" viewBox="0 0 28 28" fill="#fff"><path d="M8 17c0-4 2-6 5-7l-1 2c-1 .5-2 1.5-2 3h2v4H8zM15 17c0-4 2-6 5-7l-1 2c-1 .5-2 1.5-2 3h2v4h-4z"/></svg></div>
  <div class="center-x person abs">John Doe<small>- &nbsp;Customer</small></div>
  <span class="dot on abs" style="left:571px"></span>
  <span class="dot abs" style="left:603px"></span>
  <span class="dot abs" style="left:636px"></span>
</section>

<!-- Gallery -->
<section class="gallery">
  <div class="tile abs" style="left:0;background:linear-gradient(135deg,#3a3a34,#b7782f 50%,#5c7a2a)" role="img" aria-label="Photo of a burger with avocado"></div>
  <div class="tile tile-red abs" style="left:240px"><h4>John Doe</h4><p>Lorem Ipsum is simply dummy text of the printing</p></div>
  <div class="tile abs" style="left:480px;background:linear-gradient(135deg,#2e2e2e,#c9a24a 50%,#6a3a6a)" role="img" aria-label="Photo of tacos on a dark table"></div>
  <div class="tile abs" style="left:720px;background:linear-gradient(160deg,#6a5a4a,#c99a6a 50%,#e7b77a)" role="img" aria-label="Photo of a guest enjoying a meal"></div>
  <div class="tile abs" style="left:960px;background:linear-gradient(135deg,#6a6a6a,#d8b56a 45%,#a24a2a)" role="img" aria-label="Photo of a stone oven pizza"></div>
</section>

<!-- Contact -->
<section class="contact">
  <h2 class="heading abs" style="left:122px;top:2992px;font-size:54px">Contact Us</h2>
  <p class="contact-text abs">Lorem Ipsum is simply dummy text of the printing and typesetting industry. Lorem Ipsum has</p>
  <div class="field abs" style="left:125px;top:3139px;width:225px;height:54px">Name</div>
  <div class="field abs" style="left:378px;top:3139px;width:226px;height:54px">Email</div>
  <div class="field abs" style="left:125px;top:3216px;width:479px;height:53px">Phone</div>
  <div class="field area abs" style="left:125px;top:3290px;width:479px;height:94px">Message</div>
  <div class="btn btn-red abs" style="left:125px;top:3411px;width:134px;height:34px">Submit</div>
  <div class="map-frame abs"></div>
  <div class="map abs" role="img" aria-label="Street map showing the restaurant location"></div>
</section>

<!-- Footer -->
<div class="footer-rule abs"></div>
<footer class="footer abs"></footer>
<div class="footer-brand abs">Brava Stone Oven Kitchen</div>
<div class="f-contact f-small abs" style="left:140px;top:3771px">
  <svg width="14" height="14" viewBox="0 0 14 14" fill="#bbb"><path d="M3 1l2 3-1.3 1.3a8 8 0 0 0 5 5L10 9l3 2-1 2.5C6 13 1 8 .5 2z"/></svg>555-014-2290
</div>
<div class="f-contact f-small abs" style="left:140px;top:3797px">
  <svg width="14" height="11" viewBox="0 0 14 11" fill="#bbb"><path d="M0 0h14v11H0zM1 1.5 7 6l6-4.5"/></svg>hello@bravalinwell.example
</div>
<span class="soc abs" style="left:136px;background:#3b5998" aria-label="Social link"></span>
<span class="soc abs" style="left:182px;background:#1da1f2" aria-label="Social link"></span>
<span class="soc abs" style="left:230px;background:var(--red)" aria-label="Social link"></span>
<div class="f-small abs" style="left:134px;top:3902px;font-size:11px">Copyright © 2021 Brava</div>

<div class="f-head abs" style="left:480px;top:3692px">Dining Hours</div>
<div class="f-small abs" style="left:480px;top:3736px;line-height:22px">Courtyard is open<br>Thursday to Sunday<br>12:00pm – 9:00pm</div>
<div class="f-head abs" style="left:480px;top:3835px">Pickup &amp; Kitchen Hours</div>
<div class="f-small abs" style="left:480px;top:3881px;line-height:22px">Thursday to Sunday<br>12:00pm – 8:00pm</div>

<div class="f-head abs" style="left:801px;top:3692px">Pages</div>
<div class="f-link abs" style="left:798px;top:3749px">Home</div>
<div class="f-link abs" style="left:798px;top:3780px">About Us</div>
<div class="f-link abs" style="left:798px;top:3811px">Pages</div>
<div class="f-link abs" style="left:798px;top:3842px;border-bottom:0">Menu</div>
<div class="f-link abs" style="left:967px;top:3749px">Shop</div>
<div class="f-link abs" style="left:967px;top:3780px">Gift Cards</div>
<div class="f-link abs" style="left:967px;top:3811px;border-bottom:0">Contact</div>

</body>
</html>
```